Leadership Brenvale Brochure Design*

We host a local leadership development program every two years. We need a brochure to promote the program. We would like it to be 8 1/2 x 11, tri-fold. I have attached a Word document with the necessary info for the brochure. The brochure will be professionally printed. We would like the final design to be in InDesign.

Target Market(s)

Potential participants of our leadership program. They will be local leaders, male and female, from 30-60 years of age.

Requirements
Must have
• Content as detailed in the Word document attached. Our logo.
Nice to have
• A design that is attractive to young professionals.

```html
<!DOCTYPE html>
<html lang="en">
<head>
<meta charset="utf-8">
<title>Leadership Brenvale Brochure</title>
<link href="https://fonts.googleapis.com/css2?family=Montserrat:wght@500;600;700&family=Arimo:wght@400;700&family=Tinos:ital,wght@1,700&display=swap" rel="stylesheet">
<style>
  :root{
    --page-bg:#dcdcdc;
    --blue:#3345b0;
    --blue-dark:#24349a;
    --white:#ffffff;
    --paper:#ebebec;
    --ink:#1f1f24;
    --charcoal:#2e2e30;
    --charcoal-light:#5d5d60;
    --tag-bg:#d6d6d8;
  }
  *{box-sizing:border-box;margin:0;padding:0}
  html,body{width:1200px;height:800px;overflow:hidden;background:var(--page-bg)}
  body{font-family:"Arimo",Arial,sans-serif;position:relative}
  .brochure{position:absolute;left:150px;top:50px;width:900px;height:700px;display:flex;box-shadow:0 6px 24px rgba(0,0,0,.18)}
  .panel{position:relative;width:300px;height:700px;overflow:hidden}

  /* Testimonials panel */
  .panel--testimonials{background:var(--blue);color:var(--white)}
  .frame-line{position:absolute;left:18px;right:14px;height:1px;background:var(--white)}
  .frame-line--top{top:22px}
  .frame-line--bottom{bottom:20px}
  .testimonials__heading{position:absolute;left:42px;top:42px;width:232px;height:52px;border-top:1px solid var(--white);border-bottom:1px solid var(--white);font-family:"Montserrat",sans-serif;font-weight:600;font-size:16.5px;line-height:22px;padding:4px 0 0 30px;letter-spacing:.3px}
  .testimonials__heading .mark{position:absolute;font-family:"Tinos",serif;font-style:italic;font-size:30px;line-height:1}
  .mark--open{left:-2px;top:2px}
  .mark--close{right:-14px;bottom:-14px}
  .alumnus{position:absolute;left:37px;width:245px}
  .alumnus__head{display:flex;gap:10px;align-items:stretch}
  .alumnus__photo{width:56px;height:68px;border:2px solid var(--white);background:linear-gradient(160deg,#9a9a9a,#4c4c4c)}
  .alumnus__card{flex:1;background:var(--white);color:var(--blue);padding:9px 6px;font-size:9.5px;line-height:12px}
  .alumnus__name{font-weight:700;font-size:11px;line-height:14px}
  .alumnus__quote{margin-top:14px;font-size:9.4px;line-height:12.1px}
  .alumnus--one{top:110px}
  .alumnus--two{top:304px}

  /* Info panel */
  .panel--info{background:var(--paper);color:var(--ink)}
  .info-block{position:absolute;left:18px;width:266px}
  .info-block__title{display:flex;align-items:center;gap:14px;font-family:"Montserrat",sans-serif;font-weight:600;font-size:13.5px;color:var(--blue-dark);height:30px}
  .info-block__title svg{width:28px;height:28px;flex:none}
  .info-block__text{margin-top:10px;font-size:10.2px;line-height:12.1px}
  .info-block--attendance{top:38px}
  .info-block--tuition{top:140px}
  .info-block--apply{top:285px}
  .brand{display:flex;align-items:center;justify-content:center;gap:6px;font-family:"Montserrat",sans-serif;font-weight:700;color:var(--blue-dark);text-transform:uppercase;text-align:center}
  .brand__dot{width:14px;height:14px;border-radius:50%;background:var(--blue-dark);flex:none}
  .brand--info{position:absolute;top:510px;left:0;right:0;font-size:15px;line-height:17px}
  .contact{position:absolute;top:575px;left:0;right:0;text-align:center;font-family:"Montserrat",sans-serif;font-weight:600;font-size:13px;line-height:19px}
  .contact__phone{color:var(--blue-dark);font-weight:700;font-size:14.5px}
  .contact__web{display:inline-block;margin-top:6px;background:var(--tag-bg);color:var(--blue-dark);font-size:10.5px;letter-spacing:.8px;padding:2px 5px}

  /* Cover panel */
  .panel--cover{background:var(--charcoal);color:var(--white)}
  .cover__photo{position:absolute;inset:0;background:radial-gradient(ellipse at 50% 55%,#8a8a8c 0%,#5a5a5c 40%,#2a2a2c 100%)}
  .cover__quote{position:absolute;left:16px;top:14px;width:272px;height:180px;background:rgba(40,40,42,.85);border:1px solid rgba(255,255,255,.15);font-family:"Tinos",serif;font-style:italic;font-weight:700;text-align:center;font-size:17px;line-height:24px;padding:20px 10px 0}
  .cover__quote .big{font-size:30px}
  .cover__logo{position:absolute;left:55px;top:488px;width:192px;height:96px;background:var(--white);display:flex;align-items:center;justify-content:center}
  .brand--cover{font-size:15px;line-height:17px}
  .cover__sponsors{position:absolute;top:600px;left:0;right:0;text-align:center;font-size:10.5px;line-height:16px}
</style>
</head>
<body>
<main class="brochure">

  <section class="panel panel--testimonials">
    <div class="frame-line frame-line--top"></div>
    <h2 class="testimonials__heading"><span class="mark mark--open">“</span>What Community Alumni are saying<span class="mark mark--close">”</span></h2>

    <article class="alumnus alumnus--one">
      <div class="alumnus__head">
        <div class="alumnus__photo" role="img" aria-label="Portrait photo of Dana Whitlock"></div>
        <div class="alumnus__card">
          <p class="alumnus__name">Dana Whitlock</p>
          <p>Co-Owner, Maple Smokehouse</p>
        </div>
      </div>
      <p class="alumnus__quote">“Leadership Brenvale was an awesome experience! I learned many interesting things about the county that I have lived in all my life. We had very informative panel discussions and the tours of local attractions, including the Ridgeway Correctional Facility were eye opening! I enjoyed learning and working beside a great group of folks who are taking leadership roles in our communities to make our county a better place to live, work and play.”</p>
    </article>

    <article class="alumnus alumnus--two">
      <div class="alumnus__head">
        <div class="alumnus__photo" role="img" aria-label="Portrait photo of Owen R. Talbot"></div>
        <div class="alumnus__card">
          <p class="alumnus__name">Owen R. Talbot</p>
          <p>CPA, Partner/Manager of the Ashford Office</p>
          <p>Hale Marston &amp; Associates, LLP</p>
        </div>
      </div>
      <p class="alumnus__quote">“For the first year and a half I was working at Hale Marston, I commuted from Baywater, so I was not involved in the community at all. Once we moved here, I knew I wanted and felt I had to become more involved. I learned about the program through a colleague. I couldn’t have asked for a better experience and it really exposed me to the many ways that I could get involved and contribute to the chamber and our community. I didn’t know a soul in that 2014 class when it started and now many of them are my very best friends. If you have an opportunity to go through Leadership Brenvale you would be crazy to pass it up. It is the best program the Chamber has and, quite frankly, one of the best opportunities to better yourself in this community.”</p>
    </article>
    <div class="frame-line frame-line--bottom"></div>
  </section>

  <section class="panel panel--info">
    <div class="info-block info-block--attendance">
      <h3 class="info-block__title">
        <svg viewBox="0 0 28 28" aria-hidden="true"><path d="M14 1l3.4 2.5 4.2-.2 1.2 4 3.5 2.4-1.4 4 1.4 4-3.5 2.4-1.2 4-4.2-.2L14 27l-3.4-2.5-4.2.2-1.2-4L1.7 18.3l1.4-4-1.4-4 3.5-2.4 1.2-4 4.2.2z" fill="var(--blue-dark)"/><path d="M9 14.5l3.3 3.3L19.5 10.6" fill="none" stroke="#fff" stroke-width="2.2"/></svg>
        Attendance Policy
      </h3>
      <p class="info-block__text">Attendance at all sessions including the opening retreat is compulsory. Participants may miss no more than one session to graduate; however, the Organizational Retreat is mandatory.</p>
    </div>

    <div class="info-block info-block--tuition">
      <h3 class="info-block__title">
        <svg viewBox="0 0 28 28" aria-hidden="true"><rect x="2" y="2" width="24" height="24" rx="3" fill="var(--blue-dark)"/><g stroke="#fff" stroke-width="1.8"><path d="M6 8l1.5 1.5L10 7M6 14l1.5 1.5L10 13M6 20l1.5 1.5L10 19"/><path d="M12.5 8.5h9M12.5 14.5h9M12.5 20.5h9"/></g></svg>
        Tuition
      </h3>
      <p class="info-block__text">If accepted in the Leadership Brenvale program, you or your employer/sponsor will be invoiced $400 for Chamber members and $500 for non-members. This fee covers costs for the retreat, classroom sessions, lunches, and graduation. No refunds will be provided for participants who drop out of the program or do not fulfill the required curriculum.</p>
    </div>

    <div class="info-block info-block--apply">
      <h3 class="info-block__title">
        <svg viewBox="0 0 28 28" aria-hidden="true"><circle cx="11" cy="8" r="6" fill="var(--blue-dark)"/><path d="M1 27c0-7 4.5-11 10-11s10 4 10 11z" fill="var(--blue-dark)"/><circle cx="21" cy="21" r="6" fill="var(--blue-dark)" stroke="var(--paper)" stroke-width="1.5"/><path d="M18 21l2 2 4-4" fill="none" stroke="#fff" stroke-width="1.6"/></svg>
        To Apply
      </h3>
      <p class="info-block__text">Applications are available on the Chamber’s website, www.TheBrenvaleChamber.com Applications are due by November 2, 2020.Class size is limited. All applications received by the deadline will be reviewed and final participants for the Leadership Brenvale class will be contacted on December 4, 2020. However, all applicants will be notified of the status of their application in writing.</p>
    </div>

    <div class="brand brand--info"><span class="brand__dot"></span><span>Leadership<br>Brenvale</span></div>

    <div class="contact">
      <p>For questions, please call the<br>Chamber, <span class="contact__phone">555-014-2290</span></p>
      <p class="contact__web">www.TheBrenvaleChamber.com</p>
    </div>
  </section>

  <section class="panel panel--cover">
    <div class="cover__photo" role="img" aria-label="Black and white aerial photo of a rowing crew in a long boat on dark water"></div>
    <blockquote class="cover__quote">
      “ <span class="big">The</span> greatest wealth of a community lies not in the amount of its treasure, but in the quality of its <span class="big">Leadership.”</span>
    </blockquote>
    <div class="cover__logo">
      <div class="brand brand--cover"><span class="brand__dot"></span><span>Leadership<br>Brenvale</span></div>
    </div>
    <div class="cover__sponsors">
      <p>Sponsored by:</p>
      <p>Northfield Community College</p>
      <p>Brenvale Chamber of Commerce and Tourism</p>
    </div>
  </section>

</main>
</body>
</html>
```